Design profile for MuroDeck Nordhaven

I had a logo competition here recently, and was left with two logos that I could not choose between. Therefore, I create this competition where I want a complete design package or a visual identity for the company. I want you to create design elements that can be used both in print and online. (letterhead, envelopes, business card, website, facebook, etc.) I have also attached a picture of the car I have ordered. I'm happy if you can show how the design can be used on that as well.
What is important is that the logos are treated individually, and that the design you create reflects or builds up under the logo. I want the design to be recognizable and to have a connection with the logo and what we do. (take fizzo lumo as an example. if you remove the name, but keep the red color and the white line, then you will recognize which brand it is about right away)
You choose whether you want to make proposals only for one logo, or or both, but it is important that they are treated individually. The best overall package determines which logo I use.
I have also added an image that you can use as an example background if you want it in a facebook banner for example.
It is important that the design looks professional and unique. A number of designs have come in, but many of the designs are very similar and general. Here is a video of the printer if you need inspiration: https://clipvault.example/v/Q8ZtrMx2LwK

Industry/Entity Type

WallPrinting

Requirements
Must have
• Unique an professional design that can be used both online and print
Nice to have
• Show how to use the design on a VX Tully. (see photos attached)
Should not have
• The design can be simple, but not too simple and general. I want it to give the company an identity

```html
<!DOCTYPE html>
<html lang="en">
<head>
<meta charset="utf-8">
<title>MuroDeck Nordhaven – Letterhead</title>
<link href="https://fonts.googleapis.com/css2?family=Open+Sans:wght@400;700&family=Roboto:wght@400&display=swap" rel="stylesheet">
<style>
  :root {
    --backdrop: #dcdcdc;
    --paper: #f7f7f7;
    --ink: #111111;
    --body-text: #555555;
    --contact-text: #444444;
    --brand-red: #cf1f27;
    --brand-yellow: #f2cf06;
    --brand-blue: #1a97d4;
    --brand-navy: #13335f;
  }
  html, body {
    margin: 0;
    padding: 0;
    width: 1153px;
    height: 1200px;
    overflow: hidden;
    background: var(--backdrop);
  }
  .letterhead {
    position: absolute;
    left: 182px;
    top: 50px;
    width: 789px;
    height: 1100px;
    background: var(--paper);
    overflow: hidden;
    font-family: "Open Sans", sans-serif;
  }
  .brand-name {
    position: absolute;
    left: 69px;
    top: 78px;
    color: var(--ink);
    font-family: "Open Sans", sans-serif;
    font-weight: 700;
    line-height: 1;
    text-align: center;
  }
  .brand-name__main { display: block; font-size: 40px; letter-spacing: -0.5px; }
  .brand-name__sub { display: block; font-size: 13px; letter-spacing: 2.5px; margin-top: 6px; }
  .contact-list {
    position: absolute;
    left: 490px;
    top: 72px;
    margin: 0;
    padding: 0;
    list-style: none;
    font-family: "Roboto", sans-serif;
    font-size: 19px;
    line-height: 23.5px;
    color: var(--contact-text);
  }
  .contact-list li { display: flex; align-items: center; gap: 7px; }
  .contact-list svg { width: 16px; height: 16px; flex: none; }
  .letter-body {
    position: absolute;
    left: 69px;
    top: 261px;
    width: 648px;
    font-size: 14.2px;
    line-height: 21.3px;
    color: var(--body-text);
  }
  .letter-body p { margin: 0 0 21.3px; text-align: justify; }
  .letter-body .greeting, .letter-body .closing { text-align: left; }
  .signature {
    position: absolute;
    left: 69px;
    top: 823px;
    width: 95px;
    height: 88px;
    background: linear-gradient(135deg, #e9ebf0, #dfe2ea);
    border-radius: 4px;
  }
  .sender-address {
    position: absolute;
    left: 69px;
    top: 977px;
    font-family: "Roboto", sans-serif;
    font-size: 19px;
    line-height: 23.5px;
    color: var(--contact-text);
    font-style: normal;
  }
  .sender-address .sender-name { color: var(--ink); }
  .corner-pattern {
    position: absolute;
    right: 0;
    bottom: 0;
    width: 222px;
    height: 316px;
    background: linear-gradient(160deg, var(--brand-red) 0%, var(--brand-yellow) 35%, var(--brand-blue) 65%, var(--brand-navy) 100%);
    opacity: 0.35;
    clip-path: polygon(100% 0, 100% 100%, 0 100%);
  }
</style>
</head>
<body>
  <main class="letterhead">
    <div class="brand-name">
      <span class="brand-name__main">MuroDeck</span>
      <span class="brand-name__sub">NORDHAVEN</span>
    </div>

    <ul class="contact-list">
      <li>
        <svg viewBox="0 0 16 16" aria-hidden="true"><rect x="4" y="1" width="8" height="14" rx="1.5" fill="none" stroke="var(--brand-red)" stroke-width="1.6"/><circle cx="8" cy="12.5" r="0.9" fill="var(--brand-red)"/></svg>
        555.210.4437
      </li>
      <li>
        <svg viewBox="0 0 16 16" aria-hidden="true"><path d="M1 6c0-2 3-3 7-3s7 1 7 3v1h-3V5.5H4V7H1z" fill="var(--brand-red)"/><path d="M3 8h10l1 6H2z" fill="var(--brand-red)"/></svg>
        555.480.2290
      </li>
      <li>
        <svg viewBox="0 0 16 16" aria-hidden="true"><rect x="1" y="3.5" width="14" height="9" fill="var(--brand-red)"/><path d="M1 3.5l7 5 7-5M1 12.5l5-4.5M15 12.5l-5-4.5" fill="none" stroke="#fff" stroke-width="1"/></svg>
        info@murodeckmail.example
      </li>
      <li>
        <svg viewBox="0 0 16 16" aria-hidden="true"><circle cx="8" cy="8" r="7" fill="var(--brand-red)"/><path d="M5 4c2 1 1 3 3 3s1 3-1 4M10 3c0 2 2 2 3 3" fill="none" stroke="#fff" stroke-width="1.4"/></svg>
        www.murodeckweb.example
      </li>
    </ul>

    <section class="letter-body">
      <p class="greeting">Dear customer,</p>
      <p>Lorem ipsum dolor sit amet, consectetur adipisicing elit, sed do eiusmod tempor incididunt ut labore et dolore magna aliqua. Ut enim ad minim veniam, quis nostrud exercitation ullamco laboris nisi ut aliquip ex ea commodo consequat. Duis aute irure dolor in reprehenderit in voluptate velit esse cillum dolore eu fugiat nulla pariatur. Excepteur sint occaecat cupidatat non proident, sunt in culpa qui officia deserunt mollit anim id est laborum.</p>
      <p>Lorem ipsum dolor sit amet, consectetur adipisicing elit, sed do eiusmod tempor incididunt ut labore et dolore magna aliqua. Ut enim ad minim veniam, quis nostrud exercitation ullamco laboris nisi ut aliquip ex ea commodo consequat. Duis aute irure dolor in reprehenderit in voluptate velit esse cillum dolore eu fugiat nulla pariatur. Excepteur sint occaecat cupidatat non proident, sunt in culpa qui officia deserunt mollit anim id est laborum.</p>
      <p>Lorem ipsum dolor sit amet, consectetur adipisicing elit, sed do eiusmod tempor incididunt ut labore et dolore magna aliqua. Ut enim ad minim veniam, quis nostrud exercitation ullamco laboris nisi ut aliquip ex ea commodo consequat. Duis aute irure dolor in reprehenderit in voluptate velit esse cillum dolore eu fugiat nulla pariatur. Excepteur sint occaecat cupidatat non proident, sunt in culpa qui officia deserunt mollit anim id est laborum.</p>
      <p>Lorem ipsum dolor sit amet, consectetur adipisicing elit, sed do eiusmod tempor incididunt ut labore et dolore magna aliqua. Ut enim ad minim veniam, quis nostrud exercitation ullamco laboris nisi ut aliquip ex ea commodo consequat. Duis aute irure dolor in reprehenderit.</p>
      <p class="closing">Yours Sincerely,</p>
    </section>

    <div class="signature" role="img" aria-label="Handwritten signature of the sender"></div>

    <address class="sender-address">
      <span class="sender-name">MuroDeck-Nordhaven</span><br>
      48 Harbour Field Road<br>
      Lakeview Falls, ON K7P 3R2
    </address>

    <div class="corner-pattern" role="img" aria-label="Decorative pattern of red, yellow, blue and navy parallelograms in the lower right corner"></div>
  </main>
</body>
</html>
```